Personal letterhead and stationary

I am looking for someone to design letterhead and stationary set for my personal use. I want something simple and timeless with a little bit of color. I like photography, computers and writing.

```html
<!DOCTYPE html>
<html lang="en">
<head>
<meta charset="utf-8">
<title>Personal Letterhead</title>
<link rel="stylesheet" href="https://fonts.googleapis.com/css2?family=Arimo:wght@400;700&family=Open+Sans:wght@400&display=swap">
<style>
  :root {
    --accent: #db5a2f;
    --ink: #2a2829;
    --text: #1a1a1a;
    --paper: #ffffff;
    --mark: #1a1a1a;
    --icon: #3a3a3a;
  }
  html, body {
    margin: 0;
    padding: 0;
    overflow: hidden;
    background: var(--paper);
  }
  .letterhead {
    position: relative;
    width: 900px;
    height: 1200px;
    overflow: hidden;
    background: var(--paper);
    font-family: "Arimo", Arial, sans-serif;
    color: var(--text);
  }
  .crop-marks {
    position: absolute;
    inset: 0;
  }
  .brand-name {
    position: absolute;
    left: 103px;
    top: 90px;
    font-family: "Arimo", Arial, sans-serif;
    font-weight: 700;
    font-size: 32px;
    line-height: 40px;
    color: var(--ink);
    letter-spacing: 0.5px;
  }
  .contact {
    position: absolute;
    left: 641px;
    top: 58px;
    font-family: "Open Sans", Arial, sans-serif;
    font-size: 15px;
    font-style: normal;
    color: var(--text);
    line-height: 20px;
  }
  .contact-row {
    display: flex;
    align-items: center;
    gap: 8px;
    height: 20px;
  }
  .contact-row svg {
    width: 19px;
    height: 14px;
    flex: none;
  }
  .contact-indent {
    padding-left: 27px;
    letter-spacing: 0.5px;
  }
  .header-rule {
    position: absolute;
    left: 107px;
    top: 162px;
    width: 717px;
    height: 8px;
    display: flex;
  }
  .header-rule .accent { width: 204px; background: var(--accent); }
  .header-rule .ink { flex: 1; background: var(--ink); }
  .letter-body {
    position: absolute;
    left: 103px;
    top: 231px;
    width: 717px;
    font-size: 25px;
    line-height: 29.2px;
  }
  .letter-body p {
    margin: 0 0 29.2px;
  }
  .letter-body .line {
    display: block;
    white-space: nowrap;
    text-align: justify;
    text-align-last: justify;
  }
  .letter-body .line.end {
    text-align-last: left;
  }
  .sign-off {
    position: absolute;
    left: 103px;
    top: 870px;
    font-size: 25px;
    line-height: 29.2px;
  }
  .sign-off p { margin: 0 0 29px; }
  .footer-band {
    position: absolute;
    left: 35px;
    top: 1117px;
    width: 830px;
    height: 49px;
    display: flex;
  }
  .footer-band .accent { width: 414px; background: var(--accent); }
  .footer-band .ink { flex: 1; background: var(--ink); }
</style>
</head>
<body>
<main class="letterhead">

  <div class="footer-band"><span class="accent"></span><span class="ink"></span></div>

  <svg class="crop-marks" width="900" height="1200" viewBox="0 0 900 1200" aria-hidden="true">
    <g fill="none" stroke="var(--mark)" stroke-width="1">
      <circle cx="35" cy="35" r="13"/>
      <line x1="0" y1="35" x2="75" y2="35"/>
      <line x1="35" y1="0" x2="35" y2="72"/>
      <circle cx="865" cy="35" r="13"/>
      <line x1="825" y1="35" x2="900" y2="35"/>
      <line x1="865" y1="0" x2="865" y2="72"/>
      <circle cx="35" cy="1165" r="13"/>
      <line x1="0" y1="1165" x2="75" y2="1165"/>
      <line x1="35" y1="1128" x2="35" y2="1200"/>
      <circle cx="865" cy="1165" r="13"/>
      <line x1="825" y1="1165" x2="900" y2="1165"/>
      <line x1="865" y1="1128" x2="865" y2="1200"/>
    </g>
  </svg>

  <header>
    <div class="brand-name">Mara Lind</div>

    <address class="contact">
      <div class="contact-row">
        <svg viewBox="0 0 19 14" aria-hidden="true">
          <path d="M9.5 1a4 4 0 0 0-4 4c0 3 4 7 4 7s4-4 4-7a4 4 0 0 0-4-4z" fill="none" stroke="#b58a8a" stroke-width="1.3"/>
          <circle cx="9.5" cy="5" r="1.4" fill="#b58a8a"/>
        </svg>
        <span>Address.....................</span>
      </div>
      <div class="contact-indent">..................................</div>
      <div class="contact-row">
        <svg viewBox="0 0 19 14" aria-hidden="true">
          <path d="M6 3c-1.5 1-2 3-.5 6s4 4.5 5.5 4l1-1.5-2-1.5-1 .8c-1-.5-2-2-2.3-3l1-.7-.7-2.5z" fill="var(--icon)"/>
        </svg>
        <span>+01 555.014 2290</span>
      </div>
      <div class="contact-row">
        <svg viewBox="0 0 19 14" aria-hidden="true">
          <rect x="1" y="2" width="17" height="11" fill="none" stroke="var(--icon)" stroke-width="1.4"/>
          <path d="M1 2l8.5 6L18 2" fill="none" stroke="var(--icon)" stroke-width="1.4"/>
        </svg>
        <span>mara@lindmail.com</span>
      </div>
    </address>

    <div class="header-rule"><span class="accent"></span><span class="ink"></span></div>
  </header>

  <section class="letter-body">
    <p><span class="line end">Lorem ipsum dolor sit amet</span></p>
    <p>
      <span class="line">Lorem ipsum dolor sit amet, consectetur adipisicing elit, sed do</span>
      <span class="line">eiusmod tempor incididunt ut labore et dolore magna aliqua. Ut</span>
      <span class="line">enim ad minim veniam, quis nostrud exercitation ullamco laboris</span>
      <span class="line">nisi ut aliquip ex ea commodo consequat. Duis aute irure dolor in</span>
      <span class="line">reprehenderit in voluptate velit esse cillum dolore eu fugiat nulla</span>
      <span class="line">pariatur. Excepteur sint occaecat cupidatat non proident, sunt in</span>
      <span class="line end">culpa qui officia deserunt mollit anim id est laborum.</span>
    </p>
    <p>
      <span class="line">Lorem ipsum dolor sit amet, consectetur adipisicing elit, sed do</span>
      <span class="line">eiusmod tempor incididunt ut labore et dolore magna aliqua. Ut</span>
      <span class="line">enim ad minim veniam, quis nostrud exercitation ullamco laboris</span>
      <span class="line">nisi ut aliquip ex ea commodo consequat.Duis aute irure dolor in</span>
      <span class="line">reprehenderit in voluptate velit esse cillum dolore eu fugiat nulla</span>
      <span class="line end">pariatur.</span>
    </p>
    <p>
      <span class="line">Excepteur sint occaecat cupidatat non proident, sunt in culpa qui</span>
      <span class="line end">officia deserunt mollit anim id est laborum.</span>
    </p>
  </section>

  <footer class="sign-off">
    <p>Sincerely</p>
    <p>Name here</p>
  </footer>

</main>
</body>
</html>
```